Company Mission & Values Poster

I'd like an A2 Portrait Poster displaying our company's Mission & Values.
See our website for our logo, fonts, mission & values.
https://talvendo.com.au/

Our Mission: Creating homes for abundant life
Values: Love, Thinking, Team, Zoe.

Some ideas to consider:
Mission as the Headline then
A logo for each of the 4 Values and the words

Target Market(s)

Myself & my team

Industry/Entity Type

Real Estate

Font styles to use
Other font styles liked:
• Company fonts as seen on our website

```html
<!DOCTYPE html>
<html lang="en">
<head>
<meta charset="utf-8">
<title>Talvendo — Mission &amp; Values</title>
<link href="https://fonts.googleapis.com/css2?family=Gilda+Display&family=Figtree:wght@400;500&display=swap" rel="stylesheet">
<style>
  :root {
    --backdrop: #e9ebe9;
    --paper: #f7f7f7;
    --ink: #0b3a30;
    --ink-soft: #d6e0dc;
  }
  * { margin: 0; padding: 0; box-sizing: border-box; }
  html, body { width: 1200px; height: 1200px; overflow: hidden; }
  body { background: var(--backdrop); position: relative; color: var(--ink); font-family: "Figtree", sans-serif; }

  .poster { position: absolute; left: 197px; top: 30px; width: 806px; height: 1140px; background: var(--paper); }
  .poster > * { position: absolute; }

  .brand { left: 0; width: 100%; top: 68px; text-align: center; font-family: "Gilda Display", serif; font-size: 88px; line-height: 1; letter-spacing: 0.12em; padding-left: 0.12em; }
  .header-rule { left: 0; top: 211px; width: 100%; height: 1px; background: var(--ink); }

  .section-label { left: 59px; font-size: 15.5px; font-weight: 500; letter-spacing: 0.01em; padding-bottom: 3px; border-bottom: 1.5px solid var(--ink); line-height: 1.1; }
  .label-mission { top: 241px; }
  .label-values { top: 466px; }

  .headline { left: 82px; width: 642px; top: 292px; text-align: center; font-family: "Gilda Display", serif; font-size: 45px; line-height: 1.25; padding-bottom: 5px; border-bottom: 1.2px solid var(--ink); white-space: nowrap; }
  .mission-text { left: 70px; width: 666px; top: 372px; text-align: center; font-size: 16.2px; line-height: 19.6px; }

  .rail { width: 1px; background: var(--ink); }
  .rail-left { left: 33px; top: 566px; height: 382px; }
  .rail-right { left: 773px; top: 727px; height: 382px; }

  .value { left: 0; width: 100%; height: 128px; }
  .value > * { position: absolute; }
  .value-icon { left: 94px; top: 34px; width: 78px; height: 78px; border-radius: 50%; background: var(--ink-soft); }
  .value-bar { left: 193px; top: 33px; width: 1.3px; height: 77px; background: var(--ink); }
  .value-title { left: 214px; top: -10px; font-family: "Gilda Display", serif; font-size: 45px; line-height: 1.2; }
  .value-text { left: 214px; top: 44px; width: 500px; font-size: 14.3px; line-height: 17.9px; }
  .value-love { top: 540px; }
  .value-thinking { top: 668px; }
  .value-team { top: 796px; }
  .value-zoe { top: 924px; }
</style>
</head>
<body>
  <main class="poster">
    <div class="brand">TALVENDO</div>
    <div class="header-rule"></div>

    <div class="section-label label-mission">OUR MISSION</div>
    <h1 class="headline">Creating homes for abundant life.</h1>
    <p class="mission-text">We wholeheartedly believe that home is an extraordinary place: a haven where life unfolds in all its glory. Where we find solace, make cherished memories with loved ones, and savour the natural beauty that surrounds us.</p>

    <div class="section-label label-values">OUR VALUES</div>
    <div class="rail rail-left"></div>
    <div class="rail rail-right"></div>

    <section class="value value-love">
      <div class="value-icon" role="img" aria-label="Line icon of arms hugging a heart"></div>
      <div class="value-bar"></div>
      <h2 class="value-title">Love</h2>
      <p class="value-text">Our mission is founded in our love and respect for people - those we develop for, those in our teams and those in the communities we create and operate within.</p>
    </section>

    <section class="value value-thinking">
      <div class="value-icon" role="img" aria-label="Line icon of a glowing light bulb"></div>
      <div class="value-bar"></div>
      <h2 class="value-title">Thinking</h2>
      <p class="value-text">We believe in the power of thinking. Our rigorous and creative processes create beautifully considered solutions for our purchasers, the communities we develop within and the environment.</p>
    </section>

    <section class="value value-team">
      <div class="value-icon" role="img" aria-label="Line icon of a group of people cheering"></div>
      <div class="value-bar"></div>
      <h2 class="value-title">Team</h2>
      <p class="value-text">Property development is a team sport. We surround ourselves with the best designers and advisers. We strive to create an environment that allows them to do their best work and love doing it.</p>
    </section>

    <section class="value value-zoe">
      <div class="value-icon" role="img" aria-label="Line icon of branching coral"></div>
      <div class="value-bar"></div>
      <h2 class="value-title">Zoe</h2>
      <p class="value-text">Our mission is to create places for ‘Zoe’ - the Greek word for abundant life. We do this through exquisite design, quality construction and celebrating nature.</p>
    </section>
  </main>
</body>
</html>
```